MOLVT Study flyer

I need help designing a flyer for a research study that will include brain imaging in adolescents. The info is in the attached document. The study is called the Marrowby Orchard Lantern Vesper Trail (MOLVT) study. Ideally this would be returned as a document that I can edit in the future as we will have several new recruitment phases (different age groups, etc. I also would love to have a logo designed as part of this project, but I recognize that might be a separate design request.

```html
<!DOCTYPE html>
<html lang="en">
<head>
<meta charset="utf-8">
<title>MOLVT Study Recruitment Flyer</title>
<link rel="stylesheet" href="https://fonts.googleapis.com/css2?family=Lato:wght@400;700;900&display=swap">
<style>
  :root {
    --blue-deep: #00329a;
    --blue: #1c4ea6;
    --blue-text: #0a3497;
    --gold: #ffb500;
    --grey: #efeff3;
    --ink: #1b1b1f;
    --white: #ffffff;
    --rule: #5b79c4;
  }
  * { box-sizing: border-box; margin: 0; padding: 0; }
  html, body { width: 800px; height: 1200px; overflow: hidden; background: var(--white); }
  body { font-family: "Lato", Arial, sans-serif; color: var(--ink); }
  .flyer { position: relative; width: 800px; height: 1200px; overflow: hidden; background: var(--white); }

  .hero-photo {
    position: absolute; left: 0; top: 0; width: 800px; height: 309px;
    background: linear-gradient(100deg, #c9ccc4 0%, #8b8a80 40%, #6f8fae 75%, #4d6f95 100%);
  }
  .gold-band { position: absolute; left: 0; top: 309px; width: 800px; height: 124px; background: var(--gold); }

  .intro-panel {
    position: absolute; left: 21px; top: 140px; width: 338px; height: 445px;
    background: linear-gradient(to bottom, var(--blue-deep) 0, var(--blue-deep) 169px, var(--blue) 169px);
    border-bottom-right-radius: 170px;
  }
  .brand { position: absolute; left: 42px; top: 64px; display: flex; align-items: center; gap: 12px; color: var(--white); }
  .brand-mark { width: 22px; height: 22px; background: var(--gold); }
  .brand-name { font-size: 24px; font-weight: 700; line-height: 1.1; }
  .intro-question {
    position: absolute; left: 42px; top: 240px; width: 270px;
    color: var(--white); font-size: 31px; font-weight: 700; line-height: 1.22;
  }

  .hook { position: absolute; left: 404px; top: 316px; width: 380px; color: var(--blue-text); font-size: 29px; font-weight: 700; line-height: 1.18; }
  .summary { position: absolute; left: 404px; top: 460px; width: 370px; font-size: 18.5px; line-height: 1.36; }
  strong { font-weight: 700; }

  .section-title { position: absolute; color: var(--blue-text); font-size: 22px; font-weight: 700; }
  .involves-title { left: 21px; top: 612px; }

  .task-icon { position: absolute; border: 3px solid var(--gold); border-radius: 14px; background: #fff4d6; }
  .task-text { position: absolute; font-size: 17.5px; line-height: 1.36; }
  .icon-interview { left: 26px; top: 680px; width: 68px; height: 72px; }
  .icon-questionnaire { left: 404px; top: 684px; width: 72px; height: 64px; }
  .icon-visit { left: 26px; top: 794px; width: 66px; height: 70px; }
  .task-interview { left: 115px; top: 672px; width: 270px; }
  .task-questionnaire { left: 493px; top: 672px; width: 260px; }
  .task-visit { left: 115px; top: 786px; width: 610px; }

  .lower-band { position: absolute; left: 0; top: 943px; width: 800px; height: 257px; background: var(--grey); }
  .eligible-title { left: 21px; top: 965px; }
  .criteria { position: absolute; left: 21px; top: 1024px; width: 432px; list-style: none; }
  .criteria li { position: relative; padding: 8px 0 9px 28px; font-size: 17.5px; line-height: 1.3; border-bottom: 1px solid var(--rule); }
  .criteria li:last-child { border-bottom: none; }
  .criteria li svg { position: absolute; left: 1px; top: 13px; }

  .contact-panel {
    position: absolute; left: 456px; top: 902px; width: 318px; height: 298px;
    background: var(--gold); border-top-left-radius: 72px;
  }
  .contact-prompt { position: absolute; left: 484px; top: 978px; color: var(--blue-text); font-size: 18px; line-height: 1.4; }
  .contact-email {
    position: absolute; left: 484px; top: 1081px; width: 302px; height: 50px;
    background: var(--blue-deep); color: var(--white);
    font-size: 17px; font-weight: 700; display: flex; align-items: center; padding-left: 16px;
  }
</style>
</head>
<body>
<main class="flyer">
  <div class="hero-photo" role="img" aria-label="Photo of a thoughtful teenage girl with a ponytail looking into the distance"></div>
  <div class="gold-band"></div>

  <section class="intro-panel">
    <div class="brand">
      <span class="brand-mark"></span>
      <span class="brand-name">University of Harrowgate</span>
    </div>
    <h1 class="intro-question">Are you the parent of a child age 10-17?</h1>
  </section>

  <h2 class="hook">Do they worry or overthink negative emotions?</h2>
  <p class="summary">University of Harrowgate researchers are <strong>seeking girls age 10-17</strong> for a <strong>study about brain activity in emotions and decision-making</strong> and how they relate to <strong>puberty, anxiety and depression.</strong></p>

  <h3 class="section-title involves-title">Study participation involves:</h3>

  <div class="task-icon icon-interview" role="img" aria-label="Icon of a head with a brain"></div>
  <p class="task-text task-interview">One one-hour interview (online or in-person) where your <strong>child</strong> will discuss <strong>their thoughts</strong></p>

  <div class="task-icon icon-questionnaire" role="img" aria-label="Icon of leaves and a small circle"></div>
  <p class="task-text task-questionnaire">Online questionnaires<br><strong>(parent and child)</strong></p>

  <div class="task-icon icon-visit" role="img" aria-label="Icon of two emotion masks"></div>
  <p class="task-text task-visit">One two-hour visit where your child will complete an <strong>MRI scan, answer questions</strong> about their puberty stage, and have a small <strong>hair sample</strong> taken to study <strong>puberty hormones</strong></p>

  <div class="lower-band"></div>
  <h3 class="section-title eligible-title">Your child may be eligible if they:</h3>
  <ul class="criteria">
    <li><svg width="13" height="12" viewBox="0 0 13 12"><path d="M1 1 L12 6 L1 11 L4 6 Z" fill="#0a3497"/></svg>Are <strong>age 10-17</strong></li>
    <li><svg width="13" height="12" viewBox="0 0 13 12"><path d="M1 1 L12 6 L1 11 L4 6 Z" fill="#0a3497"/></svg>Tend to <strong>worry or overthink negative thoughts</strong></li>
    <li><svg width="13" height="12" viewBox="0 0 13 12"><path d="M1 1 L12 6 L1 11 L4 6 Z" fill="#0a3497"/></svg>Have <strong>not</strong> been diagnosed with <strong>psychosis, learning problems, or autism</strong></li>
  </ul>

  <div class="contact-panel"></div>
  <p class="contact-prompt">Interested in participating?<br>Want more information?<br><strong>Please contact us!</strong></p>
  <p class="contact-email">molvtstudy@harrowgate-health.edu</p>
</main>
</body>
</html>
```